**Build a unique raffle competition website**

Competition website such as the following.

Brantowrafflehub.co.uk
Quorvendrawsplace.com
Www.pemtiqo.com

Would like the website to have 3 categories.
Bronze , silver , gold.
Bronze for lower end prizes
Silver for medium end prizes
Gold for higher end prizes. (This would need to be as coming soon as will need to build more customer base)

Bronze will be iPhones , laptops etc
Silver will be cars and etc.

The website will need some sort of CMS management for me to use to change the main website landing page banner, adding competitions on with a start and end date (timed future dates) . Adding a thumb nail to
The competition with a
Setting for the number of tickets that the competition needs. Soon as the numbers sell, add banner to picture saying sold out.
CMS have the ability to remove users , add users, update details if required.
Give credit monetary value to spend on tickets if required.
CMS should be able today give me a export of names and raffle numbers so that this can be loaded into a automatic generator for a winner to be chosen.
CMS should allow for customers comments to be posted onto the website but must be approved first by administrator just incase it is bad language.

Users have the ability to select what number from the raffle , soon as they select one that number is reserved for 5 minutes otherwise released, other numbers which have been taken should be coloured in a different colour opposed to the ones not taken or still reserved.
Users can only purchase a maximum of 10 raffles from each competition draw.

Users will need to create an account, they will need to give their full name, email address (to be verified once signing up) address , telephone number , can upload their a photo of themselves if they wish too.
Should have the ability to see their transactions and ticket numbers for different competitions.
Should have the ability to change password, update address details if required.
Have a wallet where the company can reward users each time they spend £250, they get £5 credit to use on a ticket. Or if there is a special promotion month.

The website should also display at the top how many people are online (this will give a sense of how many people are on the website. (Rather than showing logged in users, show how many browsing on the site in total instead as those numbers will be higher than logged in).

Users have the ability to leave feedback but will require approval before being displayed.

Payment gateway will be required credit cards, debit cards, Zevopay etc to purchase tickets.

Finally I would like a pop up that states when someone has purchased a ticket for one of the draws. It should just state first name has brought a ticket on x draw .

The website must stand out professionally better than the competitors , must be mobile friendly.

Target Market(s)

Gambling

Industry/Entity Type

Gambling

Coding

Coded - Design and coding required

Number of Pages Required

5+ page

Requirements
Must have
• Professional theme, interactive
Nice to have
• Not to dull colours , not to very bright. Something in the middle that catches the viewers attention.

```html
<!DOCTYPE html>
<html lang="en">
<head>
<meta charset="utf-8">
<title>Vantor Draws – Competitions</title>
<link href="https://fonts.googleapis.com/css2?family=Roboto:wght@400;500;700;900&family=Poppins:wght@700;800&family=Oswald:wght@500&display=swap" rel="stylesheet">
<style>
:root{
  --navy:#0c4a8d;
  --navy-dark:#083a70;
  --orange:#f04e1c;
  --ink:#111111;
  --muted:#555555;
  --light-bg:#f4f1f1;
  --white:#ffffff;
  --black:#000000;
  --gold:#f5b800;
  --silver:#1c8fd8;
}
*{margin:0;padding:0;box-sizing:border-box}
html,body{width:1200px;height:2871px;overflow:hidden;background:var(--white)}
body{position:relative;font-family:"Roboto",sans-serif;color:var(--ink)}
.abs{position:absolute}

/* header */
.site-header{position:absolute;left:0;top:0;width:1200px;height:84px;background:var(--white);z-index:3}
.brand{position:absolute;left:114px;top:0;width:160px;height:146px;border-radius:0 0 80px 80px;background:var(--white);display:flex;align-items:center;justify-content:center;z-index:4}
.brand-name{font-family:"Roboto",sans-serif;font-weight:900;font-size:22px;color:var(--navy);text-align:center;line-height:1.05;margin-top:20px}
.main-nav{position:absolute;top:36px;left:451px;display:flex;font-size:13.5px;font-weight:500;text-transform:uppercase}
.main-nav a{color:var(--ink);text-decoration:none;position:absolute;white-space:nowrap}
.main-nav a.active{color:var(--orange);text-decoration:underline}
.caret{display:inline-block;border:5px solid transparent;border-top:6px solid var(--navy);margin-left:6px;vertical-align:-2px}
.register{position:absolute;left:933px;top:38px;font-size:11.5px;font-weight:500;color:var(--navy);text-decoration:underline}
.login{position:absolute;left:1004px;top:30px;width:64px;height:27px;border:2px solid var(--navy);color:var(--navy);font-size:13px;font-weight:500;display:flex;align-items:center;justify-content:center}

/* hero */
.hero{position:absolute;left:0;top:84px;width:1200px;height:569px;background:linear-gradient(180deg,#8a9bb2 0%,#2f3f95 45%,#1f2a6e 75%,#9aa6b8 100%)}
.hero-title{position:absolute;left:0;width:1200px;top:300px;text-align:center;font-family:"Poppins",sans-serif;font-weight:800;font-size:54px;color:var(--white);letter-spacing:0.5px}
.hero-sub{position:absolute;left:0;width:1200px;top:358px;text-align:center;font-family:"Poppins",sans-serif;font-weight:700;font-size:24px;color:var(--white)}
.btn-hero{position:absolute;left:539px;top:412px;width:122px;height:39px;background:var(--orange);border:2px solid var(--white);color:var(--white);font-weight:700;font-size:14.5px;display:flex;align-items:center;justify-content:center}
.slide-arrow{position:absolute;top:261px;width:36px;height:35px;background:#222;display:flex;align-items:center;justify-content:center}

/* section titles */
.section-title{position:absolute;left:0;width:1200px;text-align:center;font-weight:700;font-size:24px;color:var(--ink)}
.section-title::after{content:"";display:block;width:45px;height:3px;background:var(--navy);margin:18px auto 0}
.on-dark{color:var(--white)}
.on-dark::after{background:var(--white)}

/* competitions */
.comp-card{position:absolute;top:789px;width:228px;text-align:center}
.comp-image{height:234px;position:relative}
.tier{position:absolute;left:0;top:14px;height:24px;padding:0 12px;font-size:11.5px;font-weight:500;display:flex;align-items:center}
.tier.gold{background:var(--gold);color:var(--ink)}
.tier.bronze{background:var(--orange);color:var(--white)}
.tier.silver{background:var(--silver);color:var(--white)}
.comp-name{margin-top:17px;font-size:11.5px;font-weight:500;line-height:17px;text-transform:uppercase}
.comp-price{font-family:"Oswald",sans-serif;font-size:20px;color:var(--orange);margin-top:10px}
.countdown{display:inline-flex;margin-top:13px;background:#eceef2;height:41px}
.countdown div{width:37px;display:flex;flex-direction:column;align-items:center;justify-content:center;border-right:1px solid #fff}
.countdown div:last-child{border-right:none}
.countdown small{font-size:9px;font-weight:500}
.countdown b{font-size:15px;color:var(--navy);font-weight:500}
.round-arrow{position:absolute;top:889px;width:34px;height:34px;border:1.5px solid #888;border-radius:50%;display:flex;align-items:center;justify-content:center;background:var(--white)}

/* how it works */
.how{position:absolute;left:0;top:1229px;width:1200px;height:418px;background:var(--navy)}
.step{position:absolute;top:141px;width:250px;text-align:center;color:var(--white)}
.step svg{display:block;margin:0 auto}
.step h3{margin-top:44px;font-size:16px;font-weight:700;text-transform:uppercase}
.step p{margin-top:12px;font-size:12px;line-height:16.5px;color:#d6e1ef}
.divider{position:absolute;top:141px;width:1px;height:227px;background:#3a6aa3}

/* winners */
.winner-card{position:absolute;top:1792px;width:305px;height:286px;overflow:hidden}
.winner-image{height:179px;position:relative}
.winner-caption{position:absolute;left:16px;bottom:16px;color:var(--white)}
.winner-caption b{display:block;font-size:14px;font-weight:700}
.winner-caption span{font-size:10.5px}
.ribbon{position:absolute;right:-38px;top:14px;width:150px;height:26px;background:var(--orange);color:var(--white);transform:rotate(38deg);font-size:11px;display:flex;align-items:center;justify-content:center;letter-spacing:0.5px}
.winner-info{height:107px;background:var(--navy);position:relative}
.avatar{position:absolute;left:20px;top:20px;width:64px;height:64px;border-radius:50%;background:linear-gradient(160deg,#e7e9ee,#b9bfc9)}
.winner-name{position:absolute;left:105px;top:24px;color:var(--white);font-size:14.5px;font-weight:500;text-transform:uppercase}
.ticket-no{position:absolute;left:105px;top:51px;width:48px;height:28px;border:1.5px solid var(--white);color:var(--white);font-size:14px;font-weight:500;display:flex;align-items:center;justify-content:center}
.btn-all{position:absolute;left:527px;top:2119px;width:145px;height:33px;background:var(--orange);color:var(--white);font-size:11.5px;font-weight:700;display:flex;align-items:center;justify-content:center}

/* testimonials */
.testimonials{position:absolute;left:0;top:2206px;width:1200px;height:430px;background:var(--light-bg)}
.quote-card{position:absolute;top:129px;width:461px;height:219px;background:var(--white);padding:47px 36px 0 67px}
.quote-mark{position:absolute;left:30px;top:20px;font-family:Georgia,serif;font-size:48px;color:#bbbbbb;line-height:1}
.quote-card p{font-size:13px;line-height:17.8px;color:#333}
.stars{margin-top:10px;color:var(--orange);font-size:12px;letter-spacing:1px}
.quote-rule{width:31px;height:1px;background:#aaa;margin-top:12px}
.quote-by{margin-top:11px;font-size:10px;color:#333}
.quote-by b{color:var(--silver);font-weight:500}
.dots{position:absolute;top:2597px;left:564px;display:flex;gap:9px}
.dots i{width:6px;height:6px;border-radius:50%;background:#c9c9c9}
.dots i.on{background:var(--silver)}

/* footer */
.site-footer{position:absolute;left:0;top:2636px;width:1200px;height:235px;background:var(--black);color:var(--white)}
.footer-brand{position:absolute;left:131px;top:49px;width:154px;height:140px;display:flex;align-items:center;gap:10px}
.footer-brand .mark{width:24px;height:24px;border-radius:50%;background:var(--orange);flex:none}
.footer-brand span{font-size:24px;font-weight:900;line-height:1.05}
.footer-nav a{position:absolute;top:46px;color:var(--white);font-size:13.5px;text-decoration:none;text-transform:uppercase}
.follow{position:absolute;left:866px;top:90px;font-size:13px;font-weight:700}
.social{position:absolute;top:87px;width:26px;height:26px;border-radius:50%;background:#2a4fa3;color:var(--white);font-size:11px;font-weight:700;display:flex;align-items:center;justify-content:center}
.pay-name{position:absolute;left:786px;top:150px;font-size:20px;font-weight:700;color:#2b5bbd}
.pay-card{position:absolute;top:150px;width:38px;height:24px;background:var(--white);color:#1c2e6b;font-size:7px;font-weight:700;display:flex;align-items:center;justify-content:center;text-align:center;line-height:1}
.copyright{position:absolute;right:134px;top:200px;font-size:11.5px;color:#dddddd}
</style>
</head>
<body>

<header class="site-header">
  <div class="brand"><div class="brand-name">VANTOR<br>DRAWS</div></div>
  <nav class="main-nav">
    <a class="active" style="left:0">Home</a>
    <a style="left:64px">About Us</a>
    <a style="left:155px">Winners</a>
    <a style="left:241px">Competitions<span class="caret"></span></a>
    <a style="left:373px">Contact Us</a>
  </nav>
  <a class="register">REGISTER</a>
  <div class="login">LOGIN</div>
</header>

<section class="hero" role="img" aria-label="Smiling winner cheering in front of a blue SUV">
  <div class="slide-arrow" style="left:0"><svg width="12" height="16"><path d="M9 2 3 8l6 6" stroke="#fff" stroke-width="2" fill="none"/></svg></div>
  <div class="slide-arrow" style="right:0"><svg width="12" height="16"><path d="M3 2l6 6-6 6" stroke="#fff" stroke-width="2" fill="none"/></svg></div>
  <h1 class="hero-title">CAR WINNER</h1>
  <div class="hero-sub">$2K CASH WINNER</div>
  <div class="btn-hero">READ MORE</div>
</section>

<h2 class="section-title" style="top:703px">CURRENT COMPETITIONS</h2>

<div class="round-arrow" style="left:68px"><svg width="10" height="12"><path d="M7 1 2 6l5 5" stroke="#555" stroke-width="1.5" fill="none"/></svg></div>
<div class="round-arrow" style="left:1101px"><svg width="10" height="12"><path d="M3 1l5 5-5 5" stroke="#555" stroke-width="1.5" fill="none"/></svg></div>

<article class="comp-card" style="left:129px">
  <div class="comp-image" role="img" aria-label="Dark grey saloon car under a concrete bridge" style="background:linear-gradient(160deg,#8a8d91,#3a3d42)"><span class="tier gold">GOLD</span></div>
  <div class="comp-name">Lorem ipsum is simply<br>dummy text lorem</div>
  <div class="comp-price">£1258.95</div>
  <div class="countdown"><div><small>DAYS</small><b>2</b></div><div><small>HRS</small><b>23</b></div><div><small>MINS</small><b>31</b></div><div><small>SECS</small><b>15</b></div></div>
</article>
<article class="comp-card" style="left:368px">
  <div class="comp-image" role="img" aria-label="Hand holding a black smartphone" style="background:linear-gradient(160deg,#3b3f47,#141518)"><span class="tier bronze">BRONZE</span></div>
  <div class="comp-name">Lorem ipsum is simply<br>dummy text lorem</div>
  <div class="comp-price">£1000.95</div>
  <div class="countdown"><div><small>DAYS</small><b>2</b></div><div><small>HRS</small><b>23</b></div><div><small>MINS</small><b>31</b></div><div><small>SECS</small><b>15</b></div></div>
</article>
<article class="comp-card" style="left:606px">
  <div class="comp-image" role="img" aria-label="Open laptop on a desk" style="background:linear-gradient(180deg,#2d3a2c,#b8b8b6 60%,#e8e8e6)"><span class="tier silver">SILVER</span></div>
  <div class="comp-name">Lorem ipsum is simply<br>dummy text lorem</div>
  <div class="comp-price">£1158.95</div>
  <div class="countdown"><div><small>DAYS</small><b>2</b></div><div><small>HRS</small><b>23</b></div><div><small>MINS</small><b>31</b></div><div><small>SECS</small><b>15</b></div></div>
</article>
<article class="comp-card" style="left:847px">
  <div class="comp-image" role="img" aria-label="White washing machine in a bright room" style="background:linear-gradient(160deg,#f2f1ee,#d9d4cc)"><span class="tier bronze">BRONZE</span></div>
  <div class="comp-name">Lorem ipsum is simply<br>dummy text lorem</div>
  <div class="comp-price">£95.95</div>
  <div class="countdown"><div><small>DAYS</small><b>2</b></div><div><small>HRS</small><b>23</b></div><div><small>MINS</small><b>31</b></div><div><small>SECS</small><b>15</b></div></div>
</article>

<section class="how">
  <h2 class="section-title on-dark" style="top:47px">HOW IT WORKS</h2>
  <div class="step" style="left:97px">
    <svg width="70" height="68" viewBox="0 0 70 68" fill="none" stroke="#fff" stroke-width="2.5"><rect x="4" y="28" width="62" height="36" rx="3"/><path d="M4 36h62"/><circle cx="35" cy="13" r="9"/><circle cx="50" cy="20" r="9"/><text x="31" y="57" fill="#fff" stroke="none" font-size="18" font-family="Roboto">$</text></svg>
    <h3>Select your prize!</h3>
    <p>Contrary to popular belief, Lorem<br>Ipsum is not simply random text.<br>It has roots in a piec.</p>
  </div>
  <div class="divider" style="left:336px"></div>
  <div class="step" style="left:336px">
    <svg width="54" height="72" viewBox="0 0 54 72" fill="none" stroke="#fff" stroke-width="2.5"><rect x="4" y="6" width="46" height="62" rx="3"/><path d="M12 2v8M20 2v8M28 2v8M36 2v8M44 2v8M12 26l3 3 5-6M26 27h16M12 41l3 3 5-6M26 42h16M12 56l3 3 5-6M26 57h16"/></svg>
    <h3>Select your entries</h3>
    <p>Contrary to popular belief, Lorem<br>Ipsum is not simply random text.<br>It has roots in a piec.</p>
  </div>
  <div class="divider" style="left:588px"></div>
  <div class="step" style="left:589px">
    <svg width="64" height="64" viewBox="0 0 64 64" fill="none" stroke="#fff" stroke-width="2.5"><path d="M4 4h56v42H20L8 60V46H4z"/><path d="M14 16h36M14 25h36M14 34h24"/></svg>
    <h3>Answer the question</h3>
    <p>Contrary to popular belief, Lorem<br>Ipsum is not simply random text.<br>It has roots in a piec.</p>
  </div>
  <div class="divider" style="left:837px"></div>
  <div class="step" style="left:842px">
    <svg width="70" height="70" viewBox="0 0 70 70" fill="none" stroke="#fff" stroke-width="2.5"><circle cx="35" cy="35" r="31"/><ellipse cx="35" cy="35" rx="13" ry="31"/><rect x="2" y="24" width="66" height="22" rx="4" fill="#0c4a8d"/><text x="35" y="42" text-anchor="middle" fill="#fff" stroke="none" font-size="17" font-weight="900" font-family="Roboto">LIVE</text></svg>
    <h3>Wait for the live draw</h3>
    <p>Contrary to popular belief, Lorem<br>Ipsum is not simply random text.<br>It has roots in a piec.</p>
  </div>
</section>

<h2 class="section-title" style="top:1694px">PREVIOUS WINNERS</h2>

<article class="winner-card" style="left:123px">
  <div class="winner-image" role="img" aria-label="Bronze estate car under a cloudy sky" style="background:linear-gradient(180deg,#6f8aa5,#3f4a4e 70%,#2a2d2f)">
    <div class="ribbon">WINNER</div>
    <div class="winner-caption"><b>CAR</b><span>Contrary to popular belief  Lorem Ipsum is not.</span></div>
  </div>
  <div class="winner-info"><div class="avatar" role="img" aria-label="Winner portrait"></div><div class="winner-name">Daniel Morrow</div><div class="ticket-no">320</div></div>
</article>
<article class="winner-card" style="left:446px">
  <div class="winner-image" role="img" aria-label="Person watching a large television in a blue-lit room" style="background:linear-gradient(160deg,#1e5a7a,#0e1b2a 70%)">
    <div class="ribbon">WINNER</div>
    <div class="winner-caption"><b>TELEVISION</b><span>Contrary to popular belief  Lorem Ipsum is not.</span></div>
  </div>
  <div class="winner-info"><div class="avatar" role="img" aria-label="Winner portrait"></div><div class="winner-name">Daniel Morrow</div><div class="ticket-no">320</div></div>
</article>
<article class="winner-card" style="left:769px">
  <div class="winner-image" role="img" aria-label="Stainless steel double-door fridge" style="background:linear-gradient(90deg,#3c3f44,#9ea2a8 30%,#34373b 60%,#2b2d30)">
    <div class="ribbon">WINNER</div>
    <div class="winner-caption"><b>CAR</b><span>Contrary to popular belief  Lorem Ipsum is not.</span></div>
  </div>
  <div class="winner-info"><div class="avatar" role="img" aria-label="Winner portrait"></div><div class="winner-name">Daniel Morrow</div><div class="ticket-no">320</div></div>
</article>

<div class="btn-all">VIEW ALL WINNERS</div>

<section class="testimonials">
  <h2 class="section-title" style="top:44px">TESTIMONIALS</h2>
  <blockquote class="quote-card" style="left:131px">
    <span class="quote-mark">“</span>
    <p>Lorem ipsum dolor sit amet, consectetur adipiscing elit sed do eiusmod tempor incididunt ut labore et dolore magna aliqua. Ut enim ad minim veniam, quis nostrud exercitation ullamco laboris nisi ut aliquip ex ea commodo consequat. Duis aute irure .</p>
    <div class="stars">★★★★★</div>
    <div class="quote-rule"></div>
    <div class="quote-by"><b>OLIVER</b> Sydney</div>
  </blockquote>
  <blockquote class="quote-card" style="left:609px">
    <span class="quote-mark">“</span>
    <p>Lorem ipsum dolor sit amet, consectetur adipiscing elit sed do eiusmod tempor incididunt ut labore et dolore magna aliqua. Ut enim ad minim veniam, quis nostrud exercitation ullamco laboris nisi ut aliquip ex ea commodo consequat. Duis aute irure dolo,.</p>
    <div class="stars">★★★★★</div>
    <div class="quote-rule"></div>
    <div class="quote-by"><b>OLIVER</b> Sydney</div>
  </blockquote>
</section>
<div class="dots"><i></i><i></i><i class="on"></i><i></i><i></i></div>

<footer class="site-footer">
  <div class="footer-brand"><span class="mark"></span><span>VANTOR<br>DRAWS</span></div>
  <nav class="footer-nav">
    <a style="left:616px">Home</a>
    <a style="left:681px">About Us</a>
    <a style="left:771px">Winners</a>
    <a style="left:863px">Competitions</a>
    <a style="left:989px">Contact Us</a>
  </nav>
  <div class="follow">FOLLOW US :</div>
  <div class="social" style="left:973px">C</div>
  <div class="social" style="left:1008px">F</div>
  <div class="social" style="left:1042px">N</div>
  <div class="pay-name">Zevopay</div>
  <div class="pay-card" style="left:905px">Orbicard</div>
  <div class="pay-card" style="left:948px">Cardora</div>
  <div class="pay-card" style="left:991px">Findly</div>
  <div class="pay-card" style="left:1034px">Amerix<br>Pay</div>
  <div class="copyright">Copyright © 2020 All Rights Reserved</div>
</footer>

</body>
</html>
```